Redesign my business cards

I would like pretty much all the same information as my current business cards but redesigned to stand out more and be more unique photo uploaded to show my current business cards don’t mind if you want to remove or replace I for on the back

```html
<!DOCTYPE html>
<html lang="en">
<head>
<meta charset="utf-8">
<title>Brightline Detailing – Business Card</title>
<link href="https://fonts.googleapis.com/css2?family=Raleway:wght@400;800&family=Roboto:wght@400;500;700&display=swap" rel="stylesheet">
<style>
  :root {
    --navy: #0b1529;
    --sky: #5bc5de;
    --magenta: #b01f86;
    --paper: #ffffff;
    --backdrop: #e6e7e9;
    --ink: #0b1529;
  }
  * { margin: 0; padding: 0; box-sizing: border-box; }
  html, body { width: 746px; height: 1200px; overflow: hidden; background: var(--backdrop); }
  .canvas { position: relative; width: 746px; height: 1200px; }
  .card {
    position: absolute; left: 48px; width: 650px; height: 372px;
    background: var(--paper); overflow: hidden;
  }
  .card--front { top: 196px; }
  .card--back { top: 632px; }
  .card__shapes { position: absolute; inset: 0; }

  .brand { position: absolute; display: flex; flex-direction: column; align-items: center; gap: 8px; }
  .brand__dot { border-radius: 50%; background: var(--sky); }
  .brand__name {
    font-family: "Raleway", sans-serif; font-weight: 800; color: var(--sky);
    letter-spacing: 2px; text-align: center; line-height: 1.15;
  }
  .card--front .brand { left: 40px; top: 62px; width: 140px; }
  .card--front .brand__dot { width: 58px; height: 58px; }
  .card--front .brand__name { font-size: 15px; }
  .card--back .brand { left: 14px; top: 252px; width: 110px; gap: 6px; }
  .card--back .brand__dot { width: 38px; height: 38px; }
  .card--back .brand__name { font-size: 10px; letter-spacing: 1.5px; }

  .identity { position: absolute; right: 44px; top: 176px; text-align: right; }
  .identity__name {
    font-family: "Raleway", sans-serif; font-weight: 800; font-size: 40px;
    color: var(--ink); letter-spacing: -0.5px; line-height: 1;
  }
  .identity__role {
    font-family: "Raleway", sans-serif; font-weight: 400; font-size: 19px;
    color: var(--ink); letter-spacing: 0.5px; margin-top: 4px;
  }
  .contact { position: absolute; right: 44px; top: 276px; list-style: none; }
  .contact__item {
    display: flex; justify-content: flex-end; align-items: center; gap: 12px;
    font-family: "Roboto", sans-serif; font-weight: 500; font-size: 21px;
    color: var(--ink); height: 36px;
  }
  .contact__icon { width: 28px; height: 28px; flex: none; }

  .services { position: absolute; left: 218px; top: 54px; width: 400px; list-style: none; }
  .service { display: flex; align-items: flex-start; gap: 12px; margin-bottom: 22px; }
  .service__price {
    flex: none; width: 64px; height: 64px; border-radius: 50%; background: var(--magenta);
    color: var(--paper); font-family: "Roboto", sans-serif; font-weight: 500; font-size: 20px;
    display: flex; align-items: center; justify-content: center; margin-top: 2px;
  }
  .service__title {
    font-family: "Raleway", sans-serif; font-weight: 800; font-size: 17px; color: var(--ink);
  }
  .service__text {
    font-family: "Roboto", sans-serif; font-weight: 400; font-size: 12.4px;
    line-height: 1.25; color: var(--ink);
  }
</style>
</head>
<body>
<main class="canvas">

  <section class="card card--front" aria-label="Business card front">
    <svg class="card__shapes" viewBox="0 0 650 372" width="650" height="372" aria-hidden="true">
      <path d="M270 70 L303 0 L602 0 L580 46 Q570 70 546 70 Z" fill="var(--sky)"/>
      <path d="M0 0 L303 0 L166 290 Q148 329 110 329 L0 329 Z" fill="var(--navy)"/>
    </svg>
    <div class="brand">
      <span class="brand__dot"></span>
      <span class="brand__name">BRIGHTLINE<br>DETAILING</span>
    </div>
    <div class="identity">
      <h1 class="identity__name">DEAN MERCER</h1>
      <p class="identity__role">OWNER/OPERATOR</p>
    </div>
    <ul class="contact">
      <li class="contact__item">0412555019
        <svg class="contact__icon" viewBox="0 0 28 28" aria-hidden="true">
          <circle cx="14" cy="14" r="14" fill="var(--magenta)"/>
          <path d="M10 7.5 L12.5 7.5 L13.5 11 L11.8 12.4 Q13.2 15.4 15.8 16.6 L17.2 15 L20.5 16 L20.5 18.5 Q20 20.5 17.5 20.3 Q9 19 7.7 10.5 Q7.6 8 10 7.5 Z" fill="var(--paper)"/>
        </svg>
      </li>
      <li class="contact__item">brightlinedetailing@mail.com
        <svg class="contact__icon" viewBox="0 0 28 28" aria-hidden="true">
          <circle cx="14" cy="14" r="14" fill="var(--magenta)"/>
          <rect x="7.5" y="9" width="13" height="10" rx="1.5" fill="none" stroke="var(--paper)" stroke-width="1.8"/>
          <path d="M8 10 L14 14.5 L20 10" fill="none" stroke="var(--paper)" stroke-width="1.8"/>
        </svg>
      </li>
    </ul>
  </section>

  <section class="card card--back" aria-label="Business card back">
    <svg class="card__shapes" viewBox="0 0 650 372" width="650" height="372" aria-hidden="true">
      <path d="M150 36 L190 36 Q206 36 198 50 L124 186 L198 322 Q206 336 190 336 L150 336 L86 186 Z" fill="var(--sky)"/>
      <path d="M0 0 L178 0 L90 186 L178 372 L0 372 Z" fill="var(--navy)"/>
    </svg>
    <div class="brand">
      <span class="brand__dot"></span>
      <span class="brand__name">BRIGHTLINE<br>DETAILING</span>
    </div>
    <ul class="services">
      <li class="service">
        <span class="service__price">$150</span>
        <div>
          <h2 class="service__title">INTERIOR DETAIL</h2>
          <p class="service__text">Vacume &amp; deep clean of carpets &amp; upholstery or leather treatment, interior trim clean &amp; condition window polish and treatment, steam clean and stain removal</p>
        </div>
      </li>
      <li class="service">
        <span class="service__price">$250</span>
        <div>
          <h2 class="service__title">EXTERIOR DETAIL</h2>
          <p class="service__text">Extreme wash &amp; polish, exterior trim reviver &amp; protector window polish &amp; treatment, tyre dressing, engine bay cleaned</p>
        </div>
      </li>
      <li class="service">
        <span class="service__price">$350</span>
        <div>
          <h2 class="service__title">FULL EXTREME DETAIL</h2>
          <p class="service__text">Extreme wash &amp; polish, tyre dressing, engine bay cleaned, vacume &amp; deep clean of carpets &amp; upholstery or leather treatment, interior &amp; exterior trim reviver &amp; protector, window polish and treatment</p>
        </div>
      </li>
    </ul>
  </section>

</main>
</body>
</html>
```